Postcard Design

business name: COZY HOUR KEEPER. I am a mother of 2 well adjusted, successful teenage boys. I decided to start this company caring for kids who are home sick, unable to go to daycare or school, and when their parent cant stay home with them. I was also a career woman for many years, with no friends available or family nearby to help when i was in an emergency situation for childcare. I know how stressful it can be when a child gets sick suddenly and unexpectedly. I would like to help out those parents in need, that have pressing schedules and a sick child at home that they really want to take care of, but cant due to their work pressures and priorities. I want parents to know that their child is safe and I can help them when in need, at last minute. The design should show the child is safe and well cared for and the parent is at ease, able to accomplish their obligations. I have also founded a nonprofit environmental education program in which I teach children in youth summer camps. I have taught creativity arts combined with science curriculum in kindergarten to 8th grade non-formal teaching for the past 5 years. This is a small community, and many people know me. I will be handing out these postcards to local daycares and people I know.

Industry/Entity Type

Business

```html
<!DOCTYPE html>
<html lang="en">
<head>
<meta charset="utf-8">
<title>Cozy Hour Keeper – Postcard</title>
<link rel="stylesheet" href="https://fonts.googleapis.com/css2?family=Lilita+One&family=PT+Sans+Narrow:wght@400;700&display=swap">
<style>
  :root {
    --backdrop: #ece7df;
    --navy: #27467d;
    --navy-deep: #1f3568;
    --pink: #e2506d;
    --green-soft: #d7ebbb;
    --green-light: #e9f4da;
    --orange: #e8782a;
    --ink: #2a2a2a;
    --white: #ffffff;
  }
  * { box-sizing: border-box; margin: 0; padding: 0; }
  html, body { width: 1200px; height: 500px; overflow: hidden; }
  body {
    background: var(--backdrop);
    position: relative;
    font-family: "PT Sans Narrow", "Arial Narrow", sans-serif;
    color: var(--ink);
  }
  .card {
    position: absolute;
    top: 35px;
    height: 433px;
    overflow: hidden;
    box-shadow: 0 2px 6px rgba(0,0,0,.18);
  }

  /* Front */
  .card--front { left: 28px; width: 552px; background: var(--white); }
  .front__photo {
    position: absolute; inset: 0 0 120px 0;
    background: linear-gradient(160deg, #f7f4f0 0%, #ece4d9 45%, #f2e6d4 70%, #faf8f5 100%);
  }
  .front__band { position: absolute; left: 0; top: 0; width: 552px; height: 433px; }
  .front__headline {
    position: absolute; left: 138px; top: 14px; width: 364px;
    font-family: "Lilita One", "Arial Black", sans-serif;
    font-size: 32px; line-height: 1.05; text-align: center;
    color: var(--navy-deep); letter-spacing: .3px;
  }
  .front__headline span { display: block; white-space: nowrap; }
  .front__portrait {
    position: absolute; left: 44px; top: 213px; width: 216px; height: 216px;
    border-radius: 50%;
    border: 9px solid var(--orange);
    box-shadow: inset 0 0 0 3px #fff3d6, 0 0 0 2px #f6b46b;
    background: radial-gradient(circle at 50% 45%, #c9a48c 0%, #7a5a4a 45%, #3a2a24 75%, #e7e2db 100%);
  }
  .brand {
    position: absolute; text-align: center;
    font-family: "Lilita One", "Arial Black", sans-serif;
    color: var(--navy); line-height: 1;
  }
  .brand__dot {
    display: inline-block; width: 12px; height: 12px; border-radius: 50%;
    background: var(--navy); margin-bottom: 5px;
  }
  .brand__name { display: block; }
  .card--front .brand { left: 280px; top: 316px; width: 250px; font-size: 36px; }

  /* Back */
  .card--back {
    left: 612px; width: 560px;
    background: linear-gradient(180deg, var(--green-light), var(--green-soft));
  }
  .back__panel { position: absolute; left: 0; top: 0; width: 560px; height: 433px; }
  .back__content { position: absolute; left: 36px; top: 55px; width: 276px; }
  .back__lead {
    font-weight: 700; font-size: 19px; line-height: 1.22; color: var(--pink);
    margin-bottom: 14px;
  }
  .back__subhead { font-weight: 700; font-size: 16px; margin-bottom: 5px; }
  .back__body { font-size: 13.6px; line-height: 1.3; margin-bottom: 9px; }
  .card--back .brand { left: 318px; top: 18px; width: 225px; font-size: 30px; }
  .back__photo { position: absolute; left: 320px; width: 220px; }
  .back__photo--team {
    top: 112px; height: 82px;
    background: linear-gradient(120deg, #e8e4df, #c9b3a2 40%, #6d6f78 70%, #e6e2dc);
  }
  .back__photo--child {
    top: 205px; height: 98px;
    background: linear-gradient(110deg, #d8c2ac, #9aa6b8 50%, #eef0f3);
  }
  .back__cta {
    position: absolute; left: 328px; top: 314px; width: 204px; height: 48px;
    border-radius: 12px; background: var(--navy-deep);
    box-shadow: 0 0 0 2px var(--white);
    color: var(--white); font-weight: 700; font-size: 13.5px; line-height: 1.2;
    text-align: center; padding-top: 6px;
  }
  .back__phone {
    position: absolute; left: 320px; top: 372px; width: 220px;
    display: flex; align-items: center; justify-content: center; gap: 6px;
    font-weight: 700; font-size: 22px; color: var(--navy-deep);
  }
  .back__web {
    position: absolute; left: 320px; top: 402px; width: 220px; text-align: center;
    font-size: 13px; color: var(--ink);
  }
</style>
</head>
<body>

<section class="card card--front">
  <div class="front__photo" role="img" aria-label="Photo of a sick child resting in bed while a carer checks her temperature"></div>
  <svg class="front__band" viewBox="0 0 552 433" aria-hidden="true">
    <path d="M0 318 Q 280 306 552 274 L552 433 L0 433 Z" fill="var(--green-soft)"/>
    <path d="M0 318 Q 280 306 552 274" fill="none" stroke="var(--navy)" stroke-width="3"/>
  </svg>
  <h1 class="front__headline"><span>You don’t have to take</span><span>the day off again</span></h1>
  <div class="front__portrait" role="img" aria-label="Portrait photo of the caregiver"></div>
  <div class="brand">
    <span class="brand__dot"></span>
    <span class="brand__name">COZY HOUR</span>
    <span class="brand__name">KEEPER</span>
  </div>
</section>

<section class="card card--back">
  <svg class="back__panel" viewBox="0 0 560 433" aria-hidden="true">
    <defs>
      <linearGradient id="panelFade" x1="0" x2="1">
        <stop offset="0" stop-color="#f3f9ea"/>
        <stop offset="1" stop-color="#ffffff"/>
      </linearGradient>
    </defs>
    <path d="M0 0 L300 0 Q 340 216 300 433 L0 433 Z" fill="url(#panelFade)"/>
  </svg>

  <div class="back__content">
    <h2 class="back__lead">Back-up childcare is offered to parents when unexpected illness arises</h2>
    <h3 class="back__subhead">Sick Child Care at Home</h3>
    <p class="back__body">Most parents have experienced a time when they have needed trustworthy, last minute care for a sick child who cannot attend school or daycare. Some parents may have a designated caretaker become ill or have schedule conflicts. During this critical time when your child is recuperating, or you need last minute childcare, parents can trust Mara Linden . . . care.</p>
    <p class="back__body">I am a 10-year resident, Cedar Harbor mom, who would like to help parents in need. As a local parent, I have been there, and know how logistics and illness can cause stressful situations. You can count on me when your child gets sick and you need a backup. I can also work as a fill-in when your nanny is sick.</p>
  </div>

  <div class="brand">
    <span class="brand__dot"></span>
    <span class="brand__name">COZY HOUR</span>
    <span class="brand__name">KEEPER</span>
  </div>

  <div class="back__photo back__photo--team" role="img" aria-label="Photo of smiling colleagues at work"></div>
  <div class="back__photo back__photo--child" role="img" aria-label="Photo of a boy in bed having his temperature taken"></div>

  <div class="back__cta">For either a last minute request or advanced booking, call Mara at</div>
  <div class="back__phone">
    <svg width="16" height="16" viewBox="0 0 24 24" aria-hidden="true">
      <circle cx="12" cy="12" r="11" fill="none" stroke="var(--navy-deep)" stroke-width="2"/>
      <path d="M8.5 6.5c.6-.4 1.3-.2 1.6.4l.9 1.8c.2.5.1 1-.3 1.3l-.8.6c.6 1.4 1.6 2.5 3 3.1l.6-.8c.3-.4.9-.5 1.3-.3l1.8.9c.6.3.8 1 .4 1.6-.7 1.1-1.900 1.6-3.1 1.2-3-1-5.4-3.4-6.4-6.4-.4-1.2.1-2.4 1-3.4z" fill="var(--navy-deep)"/>
    </svg>
    (555) 214.7730
  </div>
  <div class="back__web">www.cozyhourkeeper.example/mara</div>
</section>

</body>
</html>
```